Business Card design for a company called Tallow Flame NI

I need a business card design for my oil fired boiler servicing company. I have a logo design already and Im just looking that incorporated into the business card design. card details; Tallow Flame NI
Oil Burner Servicing - Mid Ulster Area
Service Engineer - Owen Marsh
Mobile 07751364927
email - Tallow.Flame.NI@hearthmail.example
www.tallowflameni.example
I carry out Servicing, Commissioning, Fault Finding, Warranty Validation
Target Market(s)
home owners with oil fired central heating
Industry/Entity Type
Business
Contact Information for Business Card
Tallow Flame NI
Tell. 07751364927
Web: www.tallowflameni.example
email Tallow.Flame.NI@Hearthmail.Example
Servicing Fault Finding Commissioning Warranty Validation
Look and feel

```html
<!DOCTYPE html>
<html lang="en">
<head>
<meta charset="utf-8">
<title>Tallow Flame NI – Business Card</title>
<link href="https://fonts.googleapis.com/css2?family=Open+Sans:wght@400;600;700&display=swap" rel="stylesheet">
<style>
  :root {
    --backdrop: #e4e0da;
    --card-black: #0b0b0b;
    --lime: #c3d630;
    --lime-deep: #9fb326;
    --brand-green: #55b747;
    --title-yellow: #c9de2c;
    --text-white: #f2f2f2;
    --icon-green: #4fae3f;
  }
  html, body {
    margin: 0;
    width: 1200px;
    height: 892px;
    overflow: hidden;
    background: var(--backdrop);
    font-family: "Open Sans", Arial, sans-serif;
  }
  .canvas {
    position: relative;
    width: 1200px;
    height: 892px;
    display: flex;
    align-items: center;
    justify-content: center;
  }
  .card {
    position: relative;
    width: 1000px;
    height: 572px;
    border-radius: 34px;
    overflow: hidden;
    background: var(--card-black);
    box-shadow: 0 10px 30px rgba(0,0,0,.25);
  }
  .card__corners { position: absolute; inset: 0; }
  .brand {
    position: absolute;
    left: 55px;
    top: 170px;
    display: flex;
    align-items: center;
    gap: 22px;
  }
  .brand__dot {
    width: 110px;
    height: 110px;
    border-radius: 50%;
    background: var(--brand-green);
    flex: none;
  }
  .brand__name {
    margin: 0;
    font-weight: 600;
    font-size: 46px;
    line-height: 1;
    color: var(--brand-green);
    white-space: nowrap;
  }
  .brand__tagline {
    margin: 10px 0 0 3px;
    font-size: 13px;
    letter-spacing: 1.6px;
    text-transform: uppercase;
    color: var(--brand-green);
    white-space: nowrap;
  }
  .engineer {
    position: absolute;
    right: 230px;
    top: 140px;
    text-align: right;
  }
  .engineer__name {
    margin: 0;
    font-weight: 700;
    font-size: 38px;
    line-height: 1;
    color: var(--brand-green);
  }
  .engineer__role {
    margin: 4px 0 0;
    font-weight: 700;
    font-size: 18px;
    color: var(--title-yellow);
  }
  .contacts {
    position: absolute;
    right: 190px;
    top: 248px;
    margin: 0;
    padding: 0;
    list-style: none;
  }
  .contacts__item {
    display: flex;
    justify-content: flex-end;
    align-items: center;
    gap: 14px;
    height: 38px;
    font-weight: 600;
    font-size: 23px;
    color: var(--text-white);
    white-space: nowrap;
  }
  .contacts__icon { width: 22px; height: 22px; flex: none; }
  .services {
    position: absolute;
    right: 100px;
    top: 385px;
    margin: 0;
    font-weight: 600;
    font-size: 18px;
    color: var(--text-white);
    white-space: nowrap;
  }
</style>
</head>
<body>
<main class="canvas">
  <article class="card">
    <svg class="card__corners" viewBox="0 0 1000 572" preserveAspectRatio="none" aria-hidden="true">
      <defs>
        <linearGradient id="lime-fill" x1="0" y1="0" x2="1" y2="1">
          <stop offset="0" stop-color="#cfe23a"/>
          <stop offset="1" stop-color="#a8bc28"/>
        </linearGradient>
      </defs>
      <polygon points="700,0 1000,0 1000,343" fill="url(#lime-fill)"/>
      <polygon points="0,229 0,572 300,572" fill="url(#lime-fill)"/>
    </svg>

    <header class="brand">
      <span class="brand__dot"></span>
      <div>
        <h1 class="brand__name">Tallow Flame NI</h1>
        <p class="brand__tagline">Oil Burner Servicing - Mid Ulster Area</p>
      </div>
    </header>

    <section class="engineer">
      <h2 class="engineer__name">Owen Marsh</h2>
      <p class="engineer__role">Service Engineer</p>
    </section>

    <ul class="contacts">
      <li class="contacts__item">07751364927
        <svg class="contacts__icon" viewBox="0 0 22 22" aria-label="Phone">
          <rect width="22" height="22" rx="3" fill="var(--icon-green)"/>
          <path d="M7 5l2.5 0 1 3-1.6 1.2a8 8 0 0 0 3.9 3.9L14 11.5l3 1V15a1.5 1.5 0 0 1-1.6 1.5A10.5 10.5 0 0 1 5.5 6.6 1.5 1.5 0 0 1 7 5z" fill="#fff"/>
        </svg>
      </li>
      <li class="contacts__item">www.tallowflameni.example
        <svg class="contacts__icon" viewBox="0 0 22 22" aria-label="Website">
          <rect width="22" height="22" rx="3" fill="var(--icon-green)"/>
          <g fill="none" stroke="#fff" stroke-width="1.3">
            <circle cx="11" cy="11" r="6.5"/>
            <ellipse cx="11" cy="11" rx="3" ry="6.5"/>
            <path d="M4.5 11h13M5.5 7.5h11M5.5 14.5h11"/>
          </g>
        </svg>
      </li>
      <li class="contacts__item">Tallow.Flame.NI@Hearthmail.Example
        <svg class="contacts__icon" viewBox="0 0 22 22" aria-label="Email">
          <rect width="22" height="22" rx="3" fill="var(--icon-green)"/>
          <rect x="4.5" y="6.5" width="13" height="9" fill="none" stroke="#fff" stroke-width="1.3"/>
          <path d="M4.5 6.5l6.5 5 6.5-5" fill="none" stroke="#fff" stroke-width="1.3"/>
        </svg>
      </li>
    </ul>

    <p class="services">Servicing Fault Finding Commissioning Warranty Validation</p>
  </article>
</main>
</body>
</html>
```